“The Future” Spring Fair Poster

We are putting together a school and community fair. We need a poster designed to advertise the event and give some important information to would be attendees. We’d like the poster graphics to evoke a minimalistic and futuristic aesthetic, be bold, yet fun! We will printing the posters, so we will need for them to be at high resolution and ready to send to print.

Target Market(s)

Students, Parents, and Community members

Industry/Entity Type

School

Font styles to use
Sans Serif

Colors
33a6d7
fabb78
9d9d9d
ffffff
1b1b1b
33b8a4

Requirements
Must have
• The Future
• Birch & Harbor Spring Fair 2018
• Friday, May 18th
• 5:00-9:00pm
• Tickets Will Be Available at Select Pick up & Drop Off Times
• Come Enjoy a Futuristic Evening of Food, Music, Entertainment, & Fun!
Nice to have
• We’d love to see a bold and graphic poster with a futuristic feel!
• See the sample image below from previous event poster and additional images for mood and inspiration. Would love to see metallics (silver or metallic colors)

```html
<!DOCTYPE html>
<html lang="en">
<head>
<meta charset="utf-8">
<title>The Future – Birch &amp; Harbor Spring Fair 2018</title>
<link rel="stylesheet" href="https://fonts.googleapis.com/css2?family=Orbitron:wght@600;800;900&family=Arimo:wght@400;700&display=swap">
<style>
  :root {
    --sky-top: #5f7fae;
    --sky-mid: #8fa6c8;
    --sky-low: #b7c4d8;
    --sky-deep: #3f5b8c;
    --art-deep: #1c2e63;
    --art-blue: #33a6d7;
    --art-warm: #b7764a;
    --art-mist: #8fa6c8;
    --flap-light: #f4f6fa;
    --flap-shade: #b9c3d4;
    --gold-light: #ffe2a8;
    --gold: #fabb78;
    --gold-deep: #c98a3c;
    --white: #ffffff;
    --ink: #1b1b1b;
    --silver: #9d9d9d;
    --band: rgba(210, 205, 215, 0.55);
  }
  * { box-sizing: border-box; margin: 0; padding: 0; }
  html, body { width: 867px; height: 1200px; overflow: hidden; background: #eeeeee; }

  .poster {
    position: relative;
    width: 867px;
    height: 1200px;
    overflow: hidden;
    background:
      radial-gradient(ellipse 70% 25% at 30% 64%, rgba(255,255,255,0.4), transparent 70%),
      radial-gradient(ellipse 60% 22% at 75% 80%, rgba(255,255,255,0.3), transparent 70%),
      linear-gradient(180deg, var(--sky-deep) 0%, var(--sky-top) 40%, var(--sky-mid) 68%, var(--sky-low) 100%);
    font-family: "Arimo", Arial, sans-serif;
    color: var(--white);
  }

  .hero { position: absolute; left: 0; top: 0; width: 867px; height: 560px; }

  .info {
    position: absolute;
    left: 0; right: 0; top: 540px;
    text-align: center;
  }
  .title {
    font-family: "Orbitron", "Arial Black", sans-serif;
    font-weight: 900;
    font-size: 76px;
    letter-spacing: 2px;
    line-height: 1;
    background: linear-gradient(180deg, var(--gold-light) 0%, var(--gold) 45%, var(--gold-deep) 100%);
    -webkit-background-clip: text;
    background-clip: text;
    color: transparent;
    filter: drop-shadow(0 3px 3px rgba(27,27,27,0.45));
  }
  .subtitle {
    margin-top: 18px;
    font-family: "Orbitron", Arial, sans-serif;
    font-weight: 800;
    font-size: 32px;
    color: var(--gold);
    text-shadow: 0 2px 3px rgba(27,27,27,0.4);
  }
  .date {
    margin-top: 52px;
    font-weight: 700;
    font-size: 33px;
    text-shadow: 0 2px 3px rgba(27,27,27,0.35);
  }
  .time {
    margin-top: 14px;
    font-weight: 700;
    font-size: 33px;
    text-shadow: 0 2px 3px rgba(27,27,27,0.35);
  }
  .tickets {
    margin-top: 34px;
    font-weight: 700;
    font-size: 31px;
    line-height: 1.4;
    text-shadow: 0 2px 3px rgba(27,27,27,0.35);
  }

  .invite-band {
    position: absolute;
    left: 0; right: 0;
    top: 1070px; height: 110px;
    background: var(--band);
    display: flex;
    align-items: center;
    justify-content: center;
    text-align: center;
  }
  .invite {
    font-family: "Orbitron", Arial, sans-serif;
    font-weight: 800;
    font-size: 34px;
    line-height: 1.3;
    color: var(--gold);
    text-shadow: 0 2px 2px rgba(27,27,27,0.45);
  }
</style>
</head>
<body>
  <main class="poster">
    <svg class="hero" viewBox="0 0 867 560">
      <defs>
        <linearGradient id="artTone" x1="0" y1="0" x2="0" y2="1">
          <stop offset="0" stop-color="var(--art-deep)"/>
          <stop offset="0.45" stop-color="#34508c"/>
          <stop offset="0.75" stop-color="var(--art-warm)" stop-opacity="0.9"/>
          <stop offset="1" stop-color="var(--art-mist)"/>
        </linearGradient>
        <linearGradient id="flapLeft" x1="0" y1="0" x2="1" y2="0">
          <stop offset="0" stop-color="var(--flap-shade)"/>
          <stop offset="1" stop-color="var(--flap-light)"/>
        </linearGradient>
        <linearGradient id="flapRight" x1="1" y1="0" x2="0" y2="0">
          <stop offset="0" stop-color="var(--flap-shade)"/>
          <stop offset="1" stop-color="var(--flap-light)"/>
        </linearGradient>
      </defs>
      <path class="hero-art" role="img" aria-label="Cosmic illustration: open hands holding a glowing galaxy above clouds, with lightning below"
            d="M0 0 H867 V60 Q780 260 867 440 Q433 560 0 440 Q87 260 0 60 Z" fill="url(#artTone)"/>
      <path class="page-flap" d="M0 60 Q87 260 0 440 Q40 250 0 60 Z" fill="url(#flapLeft)"/>
      <path class="page-flap" d="M867 60 Q780 260 867 440 Q827 250 867 60 Z" fill="url(#flapRight)"/>
    </svg>

    <section class="info">
      <h1 class="title">THE FUTURE</h1>
      <p class="subtitle">Birch &amp; Harbor Spring Fair 2018</p>
      <p class="date">Friday, May 18th</p>
      <p class="time">5:00-9:00pm</p>
      <p class="tickets">Tickets Will Be Available at<br>Select Pick up &amp; Drop Off Times</p>
    </section>

    <div class="invite-band">
      <p class="invite">Come Enjoy a Futuristic Evening of<br>Food, Music, Entertainment, &amp; Fun!</p>
    </div>
  </main>
</body>
</html>
```